Full re-design of visual identity

We have just re-designed our logo and would like to apply it on our folders, business cards, stationery, and etc... we are attaching new logo + the material we need to re-design... we will provide full corel draw files to help make job easier and also because lot of icons and artwork can be still used...

any doubts we are at your disposal. thanks in advance.

Business

```html
<!DOCTYPE html>
<html lang="pt-BR">
<head>
<meta charset="utf-8">
<title>lunavia – Stationery Set</title>
<link rel="stylesheet" href="https://fonts.googleapis.com/css2?family=Open+Sans:wght@400;600;700&display=swap">
<style>
  :root{
    --bg:#ededed;
    --brand-grey:#7b7b7b;
    --brand-grey-dark:#6d6d6d;
    --brand-orange:#ee6a1f;
    --paper:#ffffff;
    --text-grey:#6f6f6f;
    --photo:#9a9590;
  }
  *{margin:0;padding:0;box-sizing:border-box}
  html,body{width:1200px;height:900px;overflow:hidden}
  body{background:var(--bg);font-family:"Open Sans",Arial,sans-serif;position:relative}

  .piece{position:absolute}

  .wordmark{display:flex;align-items:center;gap:5px;font-weight:700;letter-spacing:-.02em;line-height:1}
  .wordmark__dot{border-radius:50%;background:var(--brand-orange);flex:none}
  .tagline{font-weight:600;font-size:7px;line-height:1;margin-top:3px}

  /* business card front */
  .card-front{left:318px;top:97px;width:214px;height:122px;background:var(--brand-grey);padding:24px 22px}
  .card-front .wordmark{color:#fff;font-size:26px}
  .card-front .wordmark__dot{width:12px;height:12px}
  .card-front .tagline{color:#fff;font-size:5.5px}

  /* business card back */
  .card-back{left:318px;top:246px;width:214px;height:122px;background:var(--paper);padding:18px 12px 10px 20px}
  .card-back .wordmark{color:var(--brand-grey);font-size:22px}
  .card-back .wordmark__dot{width:10px;height:10px}
  .card-back .tagline{color:var(--brand-grey);font-size:5px}
  .card-back__name{margin-top:24px;color:var(--brand-orange);font-weight:700;font-size:9.5px}
  .card-back__role{color:var(--text-grey);font-size:6px}
  .card-back__contact{position:absolute;right:11px;bottom:10px;text-align:right;font-size:5.2px;line-height:1.55;color:var(--text-grey)}

  .accent{color:var(--brand-orange)}

  /* letterhead */
  .letterhead{left:565px;top:212px;width:585px;height:255px;background:var(--paper);padding:34px 34px}
  .letterhead .wordmark{color:var(--brand-grey);font-size:37px}
  .letterhead .wordmark__dot{width:15px;height:15px}
  .letterhead .tagline{color:var(--brand-grey);font-size:7.5px;margin-left:4px}
  .letterhead__contact{position:absolute;right:34px;top:42px;text-align:right;font-size:7px;line-height:1.5;color:var(--text-grey)}

  /* envelope */
  .envelope{left:564px;top:518px;width:586px;height:254px;background:var(--paper)}
  .envelope__flap{position:absolute;left:0;top:0;width:586px;height:254px}
  .envelope__brand{position:absolute;left:0;right:0;top:18px;display:flex;flex-direction:column;align-items:center}
  .envelope .wordmark{color:#fff;font-size:27px}
  .envelope .wordmark__dot{width:12px;height:12px}
  .envelope .tagline{color:#fff;font-size:5.5px}

  /* ID badge */
  .badge{left:198px;top:510px;width:252px;height:326px;background:var(--brand-grey);border-radius:14px;padding:50px 26px 0;color:#fff}
  .badge .wordmark{font-size:32px}
  .badge .wordmark__dot{width:14px;height:14px}
  .badge .tagline{font-size:7px}
  .badge__photo{display:block;width:82px;height:92px;margin:18px auto 0;background:linear-gradient(160deg,#b9b3ad,var(--photo) 60%,#4f4a4a)}
  .badge__name{text-align:center;font-weight:700;font-size:17px;margin-top:8px}
  .badge__role{text-align:center;font-size:10px;letter-spacing:.04em;margin-top:1px}
  .badge__url{position:absolute;left:0;right:0;bottom:22px;text-align:center;font-weight:700;font-size:12px}
</style>
</head>
<body>

  <section class="piece card-front">
    <div class="wordmark">lunavia<span class="wordmark__dot"></span></div>
    <div class="tagline">telecom · tecnologia · internet</div>
  </section>

  <section class="piece card-back">
    <div class="wordmark">lunavia<span class="wordmark__dot"></span></div>
    <div class="tagline">telecom · tecnologia · internet</div>
    <p class="card-back__name">Marco Tavares</p>
    <p class="card-back__role">PRESIDENT</p>
    <address class="card-back__contact" style="font-style:normal">
      Av. Serrana, 415 • Jd. Bela Vista<br>
      CEP 13410-000 • Campo Alto • SP<br>
      <span class="accent">T:</span> (11) 4520-3170 <span class="accent">F:</span> (11) 4520-3174<br>
      <span class="accent">www.lunavia.com.br</span>
    </address>
  </section>

  <section class="piece letterhead">
    <div class="wordmark">lunavia<span class="wordmark__dot"></span></div>
    <div class="tagline">telecom · tecnologia · internet</div>
    <address class="letterhead__contact" style="font-style:normal">
      Av. Serrana, 415 • Jd. Bela Vista<br>
      CEP 13410-000 • Campo Alto • SP<br>
      <span class="accent">T:</span> (11) 4520-3170 <span class="accent">F:</span> (11) 4520-3174<br>
      <span class="accent">www.lunavia.com.br</span>
    </address>
  </section>

  <section class="piece envelope">
    <svg class="envelope__flap" viewBox="0 0 586 254" aria-hidden="true">
      <polygon points="0,0 586,0 560,62 26,62" fill="var(--brand-grey)"/>
      <line x1="26" y1="62" x2="4" y2="254" stroke="#d8d8d8" stroke-width="1"/>
      <line x1="560" y1="62" x2="582" y2="254" stroke="#d8d8d8" stroke-width="1"/>
    </svg>
    <div class="envelope__brand">
      <div class="wordmark">lunavia<span class="wordmark__dot"></span></div>
      <div class="tagline">telecom · tecnologia · internet</div>
    </div>
  </section>

  <section class="piece badge">
    <div class="wordmark">lunavia<span class="wordmark__dot"></span></div>
    <div class="tagline">telecom · tecnologia · internet</div>
    <div class="badge__photo" role="img" aria-label="Portrait photo of the badge holder"></div>
    <p class="badge__name">Marco Tavares</p>
    <p class="badge__role">PRESIDENT</p>
    <p class="badge__url">www.lunavia.com.br</p>
  </section>

</body>
</html>
```